Non-profit sports organization needs templates for Word and InDesign

"Pelo Minis" is a non-profit organization in Talberg, which supports the recruitment of young talent by the handball clubs in Talberg. Every year we run several camps, a tournament for schoolchildren and several handball lessons at school.
During these activities there are always written information. So far we have not given much thought to the design. But since we think that a professional design will also lead to more interaction, we now turn to you as a designer.

For the communication with partners, sponsors, patrons, etc. we need a uniform appearance. Since different departments are currently working with different programs, we need a template for letters and documentation for Word and InDesign.

We will need the documentation template for project descriptions, information, etc.
The letter templates are needed to contact sponsors, authorities, patrons, etc.

Both the letter template and the documentation template should look modern. The design should be based on the existing flyers. Otherwise we have no other requirements so far.

Homepage: www.pelo-minis.ch

Target Market(s)

Letters, documentation or information to authorities, sponsors, associations, patrons, members, participants, etc.

Requirements
Must have
• In addition to the design, the templates should also contain a concept for titles, paragraphs, lists, etc. (colors / fonts / ...)

Word and Indesign templates

```html
<!DOCTYPE html>
<html lang="de">
<head>
<meta charset="utf-8">
<title>Pelo Minis – Dokumentation</title>
<link rel="stylesheet" href="https://fonts.googleapis.com/css2?family=Arimo:ital,wght@0,400;0,700;1,400;1,700&family=Roboto+Condensed:wght@300&display=swap">
<style>
  :root {
    --brand-blue: #3a9ad9;
    --light-blue: #9ccdec;
    --brand-red: #e2231a;
    --soft-red: #f17a70;
    --ink: #111111;
    --paper: #ffffff;
  }
  * { margin: 0; padding: 0; box-sizing: border-box; }
  html, body { width: 848px; height: 1200px; overflow: hidden; background: var(--paper); }
  body { font-family: "Arimo", Arial, sans-serif; color: var(--ink); }
  .page { position: relative; width: 848px; height: 1200px; overflow: hidden; }

  .side-band { position: absolute; left: 0; top: 0; width: 46px; height: 1200px; background: var(--brand-blue); }

  .brand { position: absolute; left: 54px; top: 92px; display: flex; align-items: center; gap: 8px; }
  .brand-dot { width: 22px; height: 22px; border-radius: 50%; background: var(--brand-red); }
  .brand-name { font-size: 24px; color: var(--brand-blue); font-weight: 400; white-space: nowrap; }

  .contact { position: absolute; left: 634px; top: 22px; font-size: 13.6px; line-height: 17px; }
  .contact-row { display: flex; align-items: flex-start; gap: 9px; margin-bottom: 7px; }
  .contact-row svg { width: 20px; height: 20px; flex: none; margin-top: 1px; }
  .contact-row:nth-child(2) svg { margin-top: 8px; }

  .rule-red { position: absolute; left: 184px; top: 118px; width: 664px; height: 3px; background: var(--brand-red); }
  .tagline { position: absolute; left: 184px; top: 124px; font-family: "Roboto Condensed", "Arial Narrow", sans-serif; font-weight: 300; font-size: 10.8px; color: var(--brand-blue); white-space: nowrap; }

  .content { position: absolute; left: 133px; top: 248px; width: 620px; font-size: 12.8px; line-height: 15.4px; }
  .content h1 { font-size: 17px; font-weight: 400; color: var(--brand-blue); margin-bottom: 16px; line-height: 20px; }
  .content p { margin-bottom: 15px; }
  .bullets { list-style: none; margin: 32px 0 30px 57px; }
  .bullets li { position: relative; line-height: 17.2px; font-size: 13.6px; }
  .bullets li:first-child { font-size: 12.8px; }
  .bullets li::before { content: ""; position: absolute; left: -14px; top: 6px; width: 4px; height: 4px; border-radius: 50%; background: var(--brand-blue); }
  .quote { margin: -3px 0 18px 37px; font-style: italic; font-size: 11.4px; line-height: 13.7px; }
  .signature { text-align: right; font-weight: 700; font-style: italic; font-size: 13px; margin-top: 6px; padding-right: 4px; }

  .lion-deco { position: absolute; left: 342px; top: 985px; width: 506px; height: 215px;
    background: radial-gradient(ellipse at 78% 45%, var(--soft-red) 0 30%, rgba(241,122,112,0) 48%),
                linear-gradient(100deg, rgba(156,205,236,0) 0%, var(--light-blue) 35%, var(--light-blue) 60%, rgba(156,205,236,0.4) 100%);
    border-radius: 60% 20% 0 40% / 70% 30% 0 30%; opacity: 0.9; }
  .rule-foot { position: absolute; left: 46px; top: 1141px; width: 336px; height: 3px; background: var(--light-blue); }
  .social { position: absolute; left: 73px; top: 1158px; display: flex; gap: 16px; }
  .social span { width: 21px; height: 21px; border-radius: 4px; background: var(--brand-blue); }
</style>
</head>
<body>
<div class="page">
  <div class="side-band"></div>

  <div class="brand">
    <span class="brand-dot"></span>
    <span class="brand-name">Pelo Minis</span>
  </div>

  <div class="contact">
    <div class="contact-row">
      <svg viewBox="0 0 20 20"><rect x="1" y="3" width="18" height="14" rx="3" fill="#5b7fc4"/><path d="M4 7l6 4 6-4" stroke="#fff" stroke-width="1.5" fill="none"/></svg>
      <span>info@pelo-minis.ch</span>
    </div>
    <div class="contact-row">
      <svg viewBox="0 0 20 20"><circle cx="10" cy="10" r="9" fill="#3a9ad9"/><path d="M5 10l5-4.5 5 4.5M6.5 9v5h7V9" stroke="#fff" stroke-width="1.6" fill="none"/></svg>
      <span>Pelo Minis<br>8450 Talberg</span>
    </div>
    <div class="contact-row">
      <svg viewBox="0 0 20 20"><rect x="1" y="1" width="18" height="18" rx="3" fill="#2f6fb5"/><circle cx="10" cy="10" r="5.5" stroke="#fff" stroke-width="1.2" fill="none"/><path d="M4.5 10h11M10 4.5c-3 3.5-3 7.5 0 11M10 4.5c3 3.5 3 7.5 0 11" stroke="#fff" stroke-width="1" fill="none"/></svg>
      <span>https://www.pelo-minis.ch/</span>
    </div>
  </div>

  <div class="rule-red"></div>
  <div class="tagline">Pelo Minis ist ein Verein mit Sitz in Talberg, welcher mit Events den Handballsport, insbesondere den Nachwuchs, in Talberg und Umgebung fördert.</div>

  <main class="content">
    <h1>Lorem ipsum dolor sit amet</h1>
    <p>Lorem ipsum dolor sit amet, consectetur meri odipiscing elit Mauris pretium porta turpis, semper ornare magna elementum convallis.</p>
    <p>Nulla lorem eros, hendrerit a mattis vel, elementum aliquam nisi. Etiam vel sapien mi. Cros nec varius ip&shy;sum. Interdum et malesuada fames ac ante ipsum primis in faucibus.</p>
    <ul class="bullets">
      <li>Proin euismod lobortis lacinia.</li>
      <li>Proin euismod lobortis lacinia.</li>
      <li>Proin euismod lobortis lacinia.</li>
      <li>Proin euismod lobortis lacinia.</li>
      <li>Proin euismod lobortis lacinia.</li>
    </ul>
    <p>Donee tincidunt enim et peLLentesque consequat. ALiquam vitae velit Lectus. Nam arcu vitae tortor Luctus, quis maLesuada metus rhoncus. Quisque ornare Lectus sed finibus condimentum. In at suscipit tortor, nec aLiquet est. Suspendisse potenti. Sed finibus veLit ipsum, a fermentum. PhaseLLus nec. Proin dignissim, nuLLa veL vehicuLa hendrerit, arcu urna sceLerisque nisL, non porta purus tortor in orci.</p>
    <p>Nunc nec Leo iaculis, venenatis LiguLa eget, tempus Lectus. Proin faciLisis eras a sapien sodaLes sodaLes. Curabitur pretium sed massa sed porta. NuLLa quis dui at risus uLtricies iacuLis. Curabitur vel tortor sagittis, Lobortis lacus pLacerat, euismod nibh. Class aptent taciti sociosqu ad Litora torquent per conubia nostra, per inceptos himenaeos. Integer sit amet dignissim mi.</p>
    <blockquote class="quote">Etiam commodo, lacus enim lacinla lorem urna sit amet nibh.<br>Aliquam malesuada dolor eros, nec fermentum massa commodo eu. NuLLa feLis purus, tincidunt nec uLtrices a, dictum a mauris. Maecenas Lorem augue, pellentesque pulvinar quam a, pretium finibus magna. Quisque dapibus voLutpat massa nec vestibulum. Ut porttitor ultricies magna vitae iaculis.</blockquote>
    <blockquote class="quote">Etiam commodo, lacus enim lacinla lorem urna sit amet nibh.<br>Aliquam malesuada dolor eros, nec fermentum massa commodo eu. NuLLa feLis purus, tincidunt nec uLtrices a, dictum a mauris. Maecenas Lorem augue, pellentesque pulvinar quam a, pretium finibus magna. Quisque dapibus voLutpat massa nec vestibulum. Ut porttitor ultricies magna vitae iaculis.</blockquote>
    <p class="signature">Vestibulum velit</p>
  </main>

  <div class="lion-deco" role="img" aria-label="Large decorative club mascot graphic in light blue and soft red"></div>
  <div class="rule-foot"></div>
  <div class="social" aria-label="Social media links">
    <span></span><span></span><span></span>
  </div>
</div>
</body>
</html>
```